label design for oral care product

Kindly invite you to design bottle label (114 mm*40 mm) for our product, a kind of oral care product. The GEL is different from our previous cleanser product, as the pic we uploaded for demonstration. The color of frosted glass bottle is dark green, but the cap is white. You could download the pic of bottle among the uploaded files. The logo file and label content description are attached too. Please check them. Our product is made from many kinds of natural plant extracts, which includes herb and fruit. I wish the label would make our product look high-end and reliable. And it would be better if you could give some advice on paper material and special requirements for printing, related to your design. I value the texture of label too, because I think that stands for the quality of products. No color limitation for the use of our logo.
Target Market(s)
20-40 female, who value oral health.
Colors
Designer to choose colors to be used in the design.
Look and feel
Each slider illustrates characteristics of the customer's brand and the style your logo design should communicate.

```html
<!DOCTYPE html>
<html lang="en">
<head>
<meta charset="utf-8">
<title>Aligner Gel – Label Set</title>
<link href="https://fonts.googleapis.com/css2?family=Cinzel:wght@700&family=Source+Serif+4:wght@400;700&display=swap" rel="stylesheet">
<style>
  :root {
    --bg-start: #fffaf0;
    --bg-end: #e9e1d7;
    --label-dark: #2a2914;
    --label-mid: #3a3a1d;
    --gold: #b08d5e;
    --gold-light: #cfae80;
    --logo-brown: #5a4524;
    --banner-dark: #2f2e19;
    --banner-glow: #4a4530;
    --ornament: #8f7450;
  }
  * { box-sizing: border-box; margin: 0; padding: 0; }
  html, body { width: 1200px; height: 840px; overflow: hidden; }
  body {
    background: linear-gradient(90deg, var(--bg-start) 0%, #f6f1e6 50%, var(--bg-end) 100%);
    font-family: "Source Serif 4", Georgia, serif;
    position: relative;
  }
  .label {
    position: absolute;
    top: 370px;
    width: 150px;
    height: 250px;
    color: var(--gold-light);
  }
  .label--front { left: 327px; }
  .label--back { left: 747px; }
  .label__frame { position: absolute; inset: 0; width: 150px; height: 250px; overflow: visible; }
  .label__stars {
    position: absolute; top: -16px; left: 50%; transform: translateX(-50%);
    width: 48px; height: 16px; border-radius: 24px 24px 0 0;
    background: var(--label-mid);
  }
  .label__stars-mark {
    position: absolute; left: 12px; top: 5px; width: 24px; height: 7px;
    background: var(--gold); opacity: .85; border-radius: 2px;
  }
  .brand {
    position: absolute; top: 24px; left: 0; right: 0;
    display: flex; justify-content: center; align-items: center; gap: 4px;
  }
  .brand__name {
    font-weight: 700; font-size: 19px; line-height: 16px;
    color: var(--logo-brown); text-align: center; letter-spacing: -0.5px;
  }
  .brand__dot { width: 7px; height: 7px; border-radius: 50%; background: var(--logo-brown); }
  .brand__rule {
    position: absolute; top: 62px; left: 40px; width: 70px; height: 1px; background: var(--gold);
  }
  .ornament-slot {
    position: absolute; width: 10px; height: 8px;
    background: var(--ornament); opacity: .7; border-radius: 2px;
  }
  .ornament-slot--wide {
    left: 50%; transform: translateX(-50%);
    width: 48px; height: 12px;
    background: linear-gradient(90deg, rgba(143,116,80,.4), var(--ornament), rgba(143,116,80,.4));
  }
  .name-banner {
    position: absolute; top: 88px; left: -6px; width: 162px; height: 48px;
    border: 3px solid var(--gold);
    background: radial-gradient(ellipse at 30% 50%, var(--banner-glow), var(--banner-dark) 70%);
    display: flex; align-items: center; justify-content: center;
    box-shadow: 0 6px 8px rgba(0,0,0,.35);
  }
  .name-banner::after {
    content: ""; position: absolute; inset: 3px; border: 1px solid rgba(176,141,94,.5);
  }
  .name-banner__title {
    font-family: "Cinzel", "Times New Roman", serif; font-weight: 700;
    font-size: 14.5px; letter-spacing: 2.4px; color: var(--gold); white-space: nowrap;
  }
  .name-banner__knob {
    position: absolute; top: -9px; left: 50%; transform: translateX(-50%);
    width: 44px; height: 9px; border-radius: 22px 22px 0 0;
    background: linear-gradient(var(--gold-light), var(--gold));
  }
  .tagline {
    position: absolute; top: 150px; left: 14px; right: 14px;
    font-size: 5px; line-height: 7.5px; text-align: center;
  }
  .volume {
    position: absolute; top: 172px; left: 0; right: 0; text-align: center; font-size: 6px;
  }
  .copy {
    position: absolute; left: 20px; right: 20px;
    font-size: 6.2px; line-height: 7.6px; text-align: justify;
  }
  .copy--directions { top: 80px; }
  .copy--contents { top: 129px; }
  .origin {
    position: absolute; top: 180px; left: 0; right: 0; text-align: center; font-size: 6.4px;
  }
</style>
</head>
<body>

  <section class="label label--front" aria-label="Front label">
    <div class="label__stars"><span class="label__stars-mark" role="img" aria-label="Three stars"></span></div>
    <svg class="label__frame" viewBox="0 0 150 250" aria-hidden="true">
      <path d="M0 10 Q75 -2 150 10 V250 H0 Z" fill="var(--label-dark)"/>
      <path d="M6 16 Q75 4 144 16 V214 H6 Z" fill="none" stroke="var(--gold)" stroke-width="1"/>
      <path d="M8 20 Q75 9 142 20" fill="none" stroke="var(--gold)" stroke-width=".6"/>
      <path d="M6 218 Q75 228 144 218" fill="none" stroke="var(--gold)" stroke-width="2.2"/>
      <path d="M6 228 Q75 238 144 228" fill="none" stroke="var(--gold)" stroke-width="1"/>
    </svg>
    <div class="brand"><span class="brand__name">lumen<br>leaf</span><span class="brand__dot"></span></div>
    <div class="brand__rule"></div>
    <span class="ornament-slot" style="top:76px;left:12px" role="img" aria-label="Small leaf ornament"></span>
    <span class="ornament-slot" style="top:76px;right:12px" role="img" aria-label="Small leaf ornament"></span>
    <div class="name-banner">
      <span class="name-banner__knob"></span>
      <h1 class="name-banner__title">ALIGNER GEL</h1>
    </div>
    <p class="tagline">Immune Support for Oral Health the Solution to Maintain Dental Hygiene and Strengthen Gums</p>
    <p class="volume">30 ml / 1 fl oz</p>
    <span class="ornament-slot ornament-slot--wide" style="top:189px" role="img" aria-label="Winged leaf ornament"></span>
  </section>

  <section class="label label--back" aria-label="Back label">
    <div class="label__stars"><span class="label__stars-mark" role="img" aria-label="Three stars"></span></div>
    <svg class="label__frame" viewBox="0 0 150 250" aria-hidden="true">
      <path d="M0 10 Q75 -2 150 10 V250 H0 Z" fill="var(--label-dark)"/>
      <path d="M6 16 Q75 4 144 16 V214 H6 Z" fill="none" stroke="var(--gold)" stroke-width="1"/>
      <path d="M8 20 Q75 9 142 20" fill="none" stroke="var(--gold)" stroke-width=".6"/>
      <path d="M6 218 Q75 228 144 218" fill="none" stroke="var(--gold)" stroke-width="2.2"/>
      <path d="M6 228 Q75 238 144 228" fill="none" stroke="var(--gold)" stroke-width="1"/>
    </svg>
    <span class="ornament-slot" style="top:22px;left:12px" role="img" aria-label="Small leaf ornament"></span>
    <span class="ornament-slot" style="top:22px;right:12px" role="img" aria-label="Small leaf ornament"></span>
    <div class="brand" style="top:30px"><span class="brand__name">lumen<br>leaf</span><span class="brand__dot"></span></div>
    <div class="brand__rule" style="top:68px"></div>
    <p class="copy copy--directions">Directions: Drop on the teeth directly after brushing. Or, put into clear aligners before wearing again. No need to rinse your mouth with water.</p>
    <p class="copy copy--contents">Contains: a proprietary blend of natural plant extract including Angelica, Radix Rehmanniae, Coptis, Honeysuckle, Echinacea, Sage, Chamomile, Acerola cherry.</p>
    <p class="origin">Made in Taiwan</p>
    <span class="ornament-slot ornament-slot--wide" style="top:195px" role="img" aria-label="Winged leaf ornament"></span>
    <span class="ornament-slot" style="top:201px;left:12px" role="img" aria-label="Small leaf ornament"></span>
    <span class="ornament-slot" style="top:201px;right:12px" role="img" aria-label="Small leaf ornament"></span>
  </section>

</body>
</html>
```